Ground breaking athletic gear company needs a kick ass business card

We are an American start up athletic gear company that uses a medically proven biohack to boost athletic performance. Heat kills strength and endurance. Our gear helps athletes manage heat better and ultimatley can improve them by up to 10% instantly. Nothing like it out there! Launching this summer.
We are looking for a modern, minimalist design that captures a sporty edge. Check out www.vanteluxgear.com, @vanteluxgear on pictorama for more ideas.

Target Market(s)

25-35 year olds, male and female athletes, vortexlift athletes, competitive runners

Industry/Entity Type

Business

Contact Information for Business Card

Derek Hollins
Founder
derekh@vanteluxgear.com
www.VanteluxGear.com
+1 (555) 014-2286

Font styles to use
Sans Serif

Requirements
Must have
• Logo and icon
• All contact information
• derekh@vanteluxgear.com
• +1 (555) 019-4431 M
• +1 (555) 014-2286
Nice to have
• Tag line : "Cool & Conquer"

```html
<!DOCTYPE html>
<html lang="en">
<head>
<meta charset="utf-8">
<title>Vantelux Gear — Business Card</title>
<link rel="stylesheet" href="https://fonts.googleapis.com/css2?family=Josefin+Sans:wght@400;600&display=swap">
<style>
  :root {
    --page-bg: #ecedef;
    --card-bg: #ffffff;
    --ink: #111111;
    --accent: #0aa3e8;
    --divider-shadow: rgba(0,0,0,0.18);
  }
  * { box-sizing: border-box; margin: 0; padding: 0; }
  html, body { width: 1200px; height: 800px; overflow: hidden; }
  body {
    background: var(--page-bg);
    font-family: "Josefin Sans", sans-serif;
    color: var(--ink);
    display: flex;
    align-items: center;
    justify-content: center;
    gap: 60px;
  }
  .card {
    width: 525px;
    height: 300px;
    background: var(--card-bg);
    box-shadow: 0 10px 30px rgba(0,0,0,0.12);
    position: relative;
    overflow: hidden;
  }

  /* Back: brand name */
  .card--back {
    display: flex;
    flex-direction: column;
    align-items: center;
    justify-content: center;
    gap: 10px;
  }
  .brand-word {
    font-weight: 600;
    font-size: 58px;
    letter-spacing: 8px;
    color: var(--accent);
    line-height: 1;
  }
  .brand-sub {
    font-weight: 600;
    font-size: 30px;
    letter-spacing: 8px;
    color: var(--ink);
    line-height: 1;
  }

  /* Front: brand + contact */
  .brand-block {
    position: absolute;
    left: 40px;
    top: 0;
    height: 100%;
    width: 200px;
    display: flex;
    align-items: center;
    gap: 10px;
  }
  .brand-square {
    width: 14px;
    height: 14px;
    background: var(--ink);
    flex: none;
  }
  .brand-name {
    font-weight: 400;
    font-size: 19px;
    letter-spacing: 3px;
    color: var(--ink);
    text-transform: uppercase;
  }
  .divider {
    position: absolute;
    left: 252px;
    top: 40px;
    width: 2px;
    height: 230px;
    background: linear-gradient(to bottom, transparent, var(--divider-shadow) 30%, var(--divider-shadow) 70%, transparent);
    transform: rotate(14deg);
    box-shadow: -4px 0 8px var(--divider-shadow);
  }
  .contact {
    position: absolute;
    left: 282px;
    top: 62px;
  }
  .person-name {
    font-size: 27px;
    font-weight: 400;
    color: var(--accent);
    letter-spacing: 1px;
    line-height: 1;
  }
  .person-role {
    font-size: 13px;
    letter-spacing: 1px;
    margin-top: 6px;
    margin-bottom: 18px;
  }
  .contact-list { list-style: none; }
  .contact-item {
    display: flex;
    align-items: center;
    gap: 10px;
    font-size: 12.5px;
    letter-spacing: 0.8px;
    margin-bottom: 12px;
  }
  .contact-icon {
    width: 24px;
    height: 24px;
    flex: none;
  }
</style>
</head>
<body>
  <section class="card card--back" aria-label="Card back">
    <div class="brand-word">VANTELUX</div>
    <div class="brand-sub">GEAR</div>
  </section>

  <section class="card card--front" aria-label="Card front">
    <div class="brand-block">
      <span class="brand-square"></span>
      <span class="brand-name">Vantelux Gear</span>
    </div>
    <div class="divider"></div>
    <div class="contact">
      <div class="person-name">Derek Hollins</div>
      <div class="person-role">Founder</div>
      <ul class="contact-list">
        <li class="contact-item">
          <svg class="contact-icon" viewBox="0 0 24 24" aria-hidden="true">
            <circle cx="12" cy="12" r="12" fill="#111"/>
            <path d="M9 6.5c.6 0 1.6 2.3 1.6 2.8s-1 1-1 1.5c0 1 2.6 3.6 3.6 3.6.5 0 1-1 1.5-1s2.8 1 2.8 1.6c0 1-1.2 2.3-2.3 2.3C11.6 17.3 6.7 12.4 6.7 8.8c0-1.1 1.3-2.3 2.3-2.3z" fill="#fff"/>
          </svg>
          <span>+1 (555) 014-2286</span>
        </li>
        <li class="contact-item">
          <svg class="contact-icon" viewBox="0 0 24 24" aria-hidden="true">
            <circle cx="12" cy="12" r="12" fill="#111"/>
            <rect x="6" y="8" width="12" height="8.5" fill="none" stroke="#fff" stroke-width="1.4"/>
            <path d="M6 8l6 5 6-5" fill="none" stroke="#fff" stroke-width="1.4"/>
          </svg>
          <span>derekh@vanteluxgear.com</span>
        </li>
        <li class="contact-item">
          <svg class="contact-icon" viewBox="0 0 24 24" aria-hidden="true">
            <circle cx="12" cy="12" r="12" fill="#111"/>
            <circle cx="12" cy="12" r="6" fill="none" stroke="#fff" stroke-width="1.3"/>
            <ellipse cx="12" cy="12" rx="2.6" ry="6" fill="none" stroke="#fff" stroke-width="1.1"/>
            <path d="M6 12h12" stroke="#fff" stroke-width="1.1"/>
          </svg>
          <span>www.VanteluxGear.com</span>
        </li>
      </ul>
    </div>
  </section>
</body>
</html>
```